business card for a massage therapy practice named 'Meadow and Willow Massage Studio'

I really need a trendy, yet easy on the eyes business card to complement my logo. Ideally with some gold or rose gold foil work.

My uploaded file of the logo I have in horizontal but I have a vertical version as well. Another color that is used in the website is a blush pink here and there. I'd like to see some trendy tropical leaves in the design.

```html
<!DOCTYPE html>
<html lang="en">
<head>
<meta charset="UTF-8">
<title>Meadow and Willow Massage Studio – Business Card</title>
<link href="https://fonts.googleapis.com/css2?family=Amatic+SC:wght@700&family=Questrial&display=swap" rel="stylesheet">
<style>
  :root {
    --backdrop: #ebe6df;
    --card: #f4f2ee;
    --card-edge: #e2ddd5;
    --ink-dark: #2b2521;
    --gold: #9b7b4a;
    --ink-soft: #6d655d;
    --leaf-deep: #2c5633;
    --leaf-light: #4f7d3f;
  }
  * { box-sizing: border-box; margin: 0; padding: 0; }
  html, body {
    width: 1047px;
    height: 1200px;
    overflow: hidden;
    background: var(--backdrop);
  }
  .canvas {
    position: relative;
    width: 1047px;
    height: 1200px;
  }
  .card {
    position: absolute;
    left: 252px;
    top: 100px;
    width: 542px;
    height: 1000px;
    background: var(--card);
    border: 1px solid var(--card-edge);
    border-radius: 26px;
    overflow: hidden;
    box-shadow: 0 18px 40px rgba(60, 45, 30, 0.12);
  }
  .brand {
    position: absolute;
    left: 57px;
    top: 130px;
    display: flex;
    align-items: center;
    gap: 16px;
  }
  .brand-dot {
    width: 54px;
    height: 54px;
    border-radius: 50%;
    background: var(--gold);
    flex: none;
  }
  .brand-name {
    font-family: "Questrial", sans-serif;
    font-size: 30px;
    line-height: 1.2;
    color: var(--ink-dark);
  }
  .holder {
    position: absolute;
    left: 64px;
    top: 358px;
  }
  .holder-name {
    font-family: "Amatic SC", cursive;
    font-weight: 700;
    font-size: 48px;
    letter-spacing: 1px;
    color: var(--gold);
    line-height: 1;
  }
  .holder-role {
    margin-top: 14px;
    font-family: "Questrial", sans-serif;
    font-size: 23px;
    letter-spacing: 1.5px;
    color: var(--ink-soft);
  }
  .contacts {
    position: absolute;
    left: 64px;
    top: 514px;
    list-style: none;
    font-family: "Questrial", sans-serif;
    font-size: 23px;
    color: var(--ink-soft);
  }
  .contacts li { height: 48px; }
  .contacts .label { color: var(--gold); }
  .foliage {
    position: absolute;
    left: 0;
    bottom: 0;
    width: 100%;
    height: 180px;
    background: linear-gradient(180deg, var(--leaf-light) 0%, var(--leaf-deep) 100%);
    border-radius: 60px 60px 0 0;
  }
</style>
</head>
<body>
  <main class="canvas">
    <section class="card">
      <div class="brand">
        <span class="brand-dot"></span>
        <p class="brand-name">Meadow and Willow<br>Massage Studio</p>
      </div>

      <div class="holder">
        <h1 class="holder-name">CLARA BENSON</h1>
        <p class="holder-role">Artist</p>
      </div>

      <ul class="contacts">
        <li><span class="label">Phone:</span> +123 456 789 0</li>
        <li><span class="label">Email:</span> lorem@ipsum.com</li>
        <li><span class="label">Web:</span> www.yourwebsite.com</li>
      </ul>

      <div class="foliage" role="img" aria-label="Row of green tropical monstera leaves along the bottom edge"></div>
    </section>
  </main>
</body>
</html>
```